KVAP Property Flyer - For Support Coordinators

Revamping our current brochures and social media posts for our properties. We need a clearer, simpler design that would be designed for Support Coordinators. Attached is our current brochure for reference.

Key details to highlight would include:
- Type of property: Studio Apartments with Psychosocial Disability Support located in Inner West
- Accommodation features
- Services

Our logo is also attached, please make the brochure with similar branding colours and fonts.

Designs look the same

Sick

Font styles to use
Sans Serif
Other font styles liked:
• Montserrat Light and Montserrat Semi Bold

Colors
0054AA
0677BA
7BADD7
CADEEF
E8F1F8

Requirements
Nice to have
• Please refer to this style guide: https://slides.trovelmark.com/deck/8TkwPzLmRd5VbQx2NcYh4GfJs7AeUo9WiKnBrMp3tZq/view?mode=shared

```html
<!DOCTYPE html>
<html lang="en">
<head>
<meta charset="utf-8">
<title>Harbourlight Living – Petersham Studio Apartments</title>
<link rel="stylesheet" href="https://fonts.googleapis.com/css2?family=Montserrat:wght@300;400;500;600;700;800&display=swap">
<style>
:root{
  --bg:#e5e5e5;
  --paper:#ffffff;
  --blue:#3a90c6;
  --blue-deep:#2f82b5;
  --blue-light:#5cb1de;
  --caption:rgba(62,151,201,.88);
  --ink:#3b3f47;
  --ink-soft:#555a63;
  --grey-band:#efefef;
  --line:#8a8f96;
}
*{margin:0;padding:0;box-sizing:border-box}
html,body{width:1200px;height:2400px;overflow:hidden}
body{background:var(--bg);font-family:'Montserrat',sans-serif;color:var(--ink);position:relative}
.page{position:absolute;width:494px;height:699px;background:var(--paper);box-shadow:0 3px 10px rgba(0,0,0,.18);overflow:hidden}
.abs{position:absolute}
.photo{position:absolute}

/* brand mark */
.brand{position:absolute;display:flex;flex-direction:column;align-items:center;gap:6px}
.brand-dot{width:44px;height:44px;border-radius:50%;background:var(--blue-light)}
.brand-name{font-weight:400;color:var(--ink-soft);letter-spacing:.08em;white-space:nowrap}

/* ---------- cover ---------- */
.cover .hero-photo{left:0;top:51px;width:494px;height:301px;background:linear-gradient(180deg,#9cc6e8 0%,#c9dcea 40%,#6d6f70 70%,#4b4c4d 100%)}
.cover .logo-box{left:0;top:0;width:252px;height:104px;background:var(--paper);clip-path:polygon(0 0,100% 0,93% 100%,0 100%)}
.cover .logo-box .brand{left:34px;top:30px}
.cover .logo-box .brand-dot{width:38px;height:38px}
.cover .logo-box .brand-name{font-size:11px}
.cover .stripe{left:218px;top:54px;width:42px;height:50px;background:var(--blue);clip-path:polygon(68% 0,100% 0,32% 100%,0 100%)}
.cover .address-bar{left:270px;top:23px;width:224px;height:29px;background:var(--ink);clip-path:polygon(8% 0,100% 0,100% 100%,0 100%);color:#fff;font-size:9px;display:flex;align-items:center;gap:5px;padding-left:26px}
.cover .title-panel{left:0;top:255px;width:350px;height:97px;background:rgba(52,56,64,.88);clip-path:polygon(0 0,86% 0,100% 100%,0 100%);color:#fff;padding:14px 0 0 27px}
.cover .title-panel h1{font-size:36px;font-weight:800;line-height:1;letter-spacing:-.01em}
.cover .title-panel p{font-size:12px;font-weight:600;line-height:1.35;margin-top:6px}
.cover .welcome{left:0;top:352px;width:494px;height:89px;background:var(--grey-band)}
.cover .welcome h2{position:absolute;left:28px;top:22px;font-size:19px;font-weight:500;line-height:1.05;color:var(--ink-soft)}
.cover .welcome h2 strong{display:block;font-size:25px;font-weight:800;color:var(--blue)}
.cover .welcome .divider{position:absolute;left:198px;top:18px;height:54px;border-left:1px dashed #888}
.cover .welcome .intro{position:absolute;left:212px;top:17px;width:258px;font-size:6.6px;line-height:1.3;text-align:justify;color:var(--ink-soft)}
.cover .welcome .intro p+p{margin-top:6px}
.list-col{position:absolute;top:456px;width:220px}
.list-col h3{font-size:12.5px;font-weight:700;color:var(--ink);margin-bottom:9px}
.list-col h3 span{color:var(--blue)}
.list-col li{list-style:none;display:flex;align-items:flex-start;gap:8px;font-size:7.6px;font-weight:500;line-height:1.3;margin-bottom:8px}
.list-col li i{flex:none;width:13px;height:13px;border-radius:50%;background:var(--blue);margin-top:-2px}
.cover .col-left{left:27px}
.cover .col-right{left:270px}
.cover .footer-band{left:0;top:615px;width:494px;height:84px;background:var(--blue-deep)}
.cover .strip{top:560px;width:150px;height:82px;clip-path:polygon(22% 0,100% 0,78% 100%,0 100%);z-index:2}
.cover .strip.a{left:30px;background:linear-gradient(160deg,#d9d6d0,#8e6e55)}
.cover .strip.b{left:170px;background:linear-gradient(160deg,#e8e8e8,#55585c)}
.cover .strip.c{left:310px;background:linear-gradient(160deg,#e2e4e6,#9fa4a8)}
.cover .find-more{left:28px;top:652px;font-size:15.5px;font-weight:700;color:#fff;letter-spacing:.02em}
.cover .vsep{top:650px;height:22px;border-left:1px dashed rgba(255,255,255,.8)}
.cover .contact{top:650px;color:#fff;font-size:7.6px;line-height:1.55}
.cover .contact div{display:flex;align-items:center;gap:5px}
.ico-dot{width:6px;height:6px;border-radius:50%;background:#fff;display:inline-block}

/* ---------- emergency page ---------- */
.emergency .brand{left:0;width:494px;top:340px;gap:12px}
.emergency .brand-dot{width:70px;height:70px}
.emergency .brand-name{font-size:23px;font-weight:400;letter-spacing:.09em}
.emergency .panel{left:0;top:497px;width:494px;height:137px;background:var(--ink)}
.emergency .pill{left:89px;top:484px;width:317px;height:27px;border-radius:12px;background:var(--blue);border:2px solid #fff;color:#fff;font-size:15px;font-weight:700;letter-spacing:.03em;display:flex;align-items:center;justify-content:center;z-index:2}
.emergency .col{top:530px;color:#fff;font-size:7.8px;line-height:1.3;font-weight:500}
.emergency .col p{margin-bottom:8px}
.emergency .col b{color:var(--blue-light);font-weight:500}
.emergency .c1{left:55px;width:200px}
.emergency .c2{left:273px;width:200px}
.emergency .mid{left:263px;top:528px;height:80px;border-left:1px dashed rgba(255,255,255,.7)}
.emergency .site{left:0;width:494px;top:647px;text-align:center;font-size:11px;font-weight:500;letter-spacing:.14em}

/* ---------- unit image pages ---------- */
.gallery .frame{left:19px;top:51px;width:458px;height:481px;border:1.3px solid var(--ink);border-bottom:none}
.gallery h2{left:0;width:494px;top:32px;text-align:center;font-size:29px;font-weight:800;letter-spacing:-.01em;line-height:1}
.gallery h2 span.inner{background:var(--paper);padding:0 10px;position:relative}
.gallery h2 .blue{color:var(--blue)}
.gallery h2 .inner::before,.gallery h2 .inner::after{content:"";position:absolute;top:50%;width:5px;height:5px;border-radius:50%;background:var(--ink);transform:translateY(-50%)}
.gallery h2 .inner::before{left:0}
.gallery h2 .inner::after{right:0}
.tile{position:absolute;box-shadow:0 0 0 3px #fff,0 2px 6px rgba(0,0,0,.25)}
.tile figcaption{position:absolute;left:0;right:0;bottom:0;height:31px;background:var(--caption);color:#fff;font-size:9.5px;font-weight:600;letter-spacing:.03em;display:flex;align-items:center;justify-content:center}
.tone-wall{background:linear-gradient(135deg,#f1f1ef,#cfd0cc)}
.tone-green{background:linear-gradient(180deg,#3c3f42 0%,#6d8e4a 45%,#9cb56d 65%,#5a5d60 100%)}
.tone-room{background:linear-gradient(135deg,#eeeeee,#b9bcbf 60%,#595c60)}
.tone-view{background:linear-gradient(180deg,#c5d7e8,#9fa59b 50%,#8a5a3e 80%,#5c4030)}
.tone-bath{background:linear-gradient(135deg,#6e857c,#e9ecea 45%,#f4f4f4)}
.tone-kitchen{background:linear-gradient(180deg,#464849,#cfd0cf 45%,#ececec)}
.page-foot .brand{left:30px;top:619px;gap:4px}
.page-foot .brand-dot{width:30px;height:30px}
.page-foot .brand-name{font-size:7.8px}
.page-foot .rule{left:112px;top:667px;width:330px;border-top:1px solid #9a9ea4}
.page-foot .tab{left:345px;top:652px;width:110px;height:16px;background:var(--ink);clip-path:polygon(7% 0,100% 0,100% 100%,0 100%);color:#fff;font-size:7px;display:flex;align-items:center;justify-content:center}
.page-foot .num{left:450px;top:651px;width:18px;height:18px;border-radius:50%;border:1.5px solid var(--ink);background:#fff;font-size:7px;font-weight:700;display:flex;align-items:center;justify-content:center}

/* ---------- transport page ---------- */
.transport .head{left:0;top:0;width:494px;height:87px;background:var(--ink)}
.transport .head h2{position:absolute;left:0;width:494px;top:25px;text-align:center;color:#fff;font-size:15.5px;font-weight:700;letter-spacing:.02em}
.transport .acc1{left:32px;top:76px;width:10px;height:12px;background:var(--blue)}
.transport .acc2{left:453px;top:288px;width:10px;height:33px;background:var(--blue)}
.transport .map{left:40px;top:59px;width:416px;height:256px;background:linear-gradient(160deg,#f3f3f1 0%,#ecebe6 55%,#f2e6c4 75%,#eeeeea 100%);box-shadow:0 1px 4px rgba(0,0,0,.2)}
.transport .lead{left:0;width:494px;top:336px;text-align:center;font-size:9.6px;font-weight:700;line-height:1.3}
.transport .lead span{color:var(--blue)}
.place{position:absolute;display:flex;height:20px;font-size:6.6px;font-weight:600}
.place .name{background:var(--ink);color:#fff;display:flex;align-items:center;gap:5px;padding-left:4px;line-height:1.15;border-radius:10px 0 0 10px}
.place .name i{flex:none;width:13px;height:13px;border-radius:50%;background:#fff;border:2px solid var(--blue-light)}
.place .time{background:var(--blue);color:#fff;font-size:8px;display:flex;align-items:center;justify-content:center;margin-left:2px}
.place.l .name{width:117px}.place.l .time{width:61px}
.place.r .name{width:116px}.place.r .time{width:62px}
.transport .bus-band{left:0;top:463px;width:494px;height:102px;background:var(--grey-band)}
.transport .bus-tab{left:147px;top:452px;width:203px;height:24px;background:var(--ink);border-radius:12px 12px 0 0;color:#fff;font-size:12.5px;font-weight:600;letter-spacing:.04em;display:flex;align-items:center;justify-content:center}
.bus{position:absolute;left:40px;width:414px;display:flex;align-items:center;font-size:7.6px;font-weight:500;height:14px}
.bus .code{width:14px;font-weight:700}
.bus .code sup{font-size:5px}
.bus .route{background:var(--blue);color:#fff;font-weight:700;width:30px;height:12px;display:flex;align-items:center;justify-content:center;margin-right:4px;font-size:7px}
.bus .dots{flex:1;border-top:1px dotted #888;margin:0 4px}
.bus .stop{white-space:nowrap}
.bus .walk{color:var(--blue);font-weight:700;white-space:nowrap}
.transport .notes{left:0;width:494px;top:581px;text-align:center;font-size:5.9px;line-height:1.6;color:var(--ink)}
.transport .notes b{font-weight:700}
</style>
</head>
<body>

<!-- Cover -->
<section class="page cover" style="left:75px;top:93px">
  <div class="photo hero-photo" role="img" aria-label="Street view of the modern Petersham apartment building beside older brick houses"></div>
  <div class="abs logo-box">
    <div class="brand"><span class="brand-dot"></span><span class="brand-name">HARBOURLIGHT LIVING</span></div>
  </div>
  <div class="abs stripe"></div>
  <div class="abs address-bar">
    <svg width="9" height="11" viewBox="0 0 10 12"><path d="M5 0a4 4 0 0 1 4 4c0 3-4 8-4 8S1 7 1 4a4 4 0 0 1 4-4z" fill="#fff"/><circle cx="5" cy="4" r="1.5" fill="#3b3f47"/></svg>
    27 Wren Street, Petersham NSW 2049
  </div>
  <div class="abs title-panel">
    <h1>PETERSHAM</h1>
    <p>Studio Apartments for people with a<br>psychosocial disability.</p>
  </div>
  <div class="abs welcome">
    <h2>WELCOME TO<strong>PETERSHAM</strong></h2>
    <span class="divider"></span>
    <div class="intro">
      <p>Located in the heart of Petersham, our new 20 self-contained studio apartments which have a kitchen with fridge, small stove top and microwave. It has a single bed, tv, dining table and bathroom. Some apartments have small balconies, and some have decks over looking the bustling suburb.</p>
      <p>Situated a 5 minute walk to Petersham Train Station, and other public transport.</p>
    </div>
  </div>
  <div class="list-col col-left">
    <h3><span>COMMUNITIES</span> &amp; FACILITIES</h3>
    <ul>
      <li><i></i>Close to shops, cafes and public transport</li>
      <li><i></i>Local GP Practice and Dentistry</li>
      <li><i></i>Commercial Space for Social Enterprise</li>
    </ul>
  </div>
  <div class="list-col col-right">
    <h3><span>FEATURES</span> &amp; SERVICES</h3>
    <ul>
      <li><i></i>24/7 Video-Intercom &amp; on site support.</li>
      <li><i></i>Disability access walkways &amp; bathroom.</li>
      <li><i></i>Trained &amp; experienced Staff in<br>psychosocial disability.</li>
    </ul>
  </div>
  <div class="abs footer-band"></div>
  <div class="photo strip a" role="img" aria-label="Studio bedroom with window"></div>
  <div class="photo strip b" role="img" aria-label="Studio kitchenette"></div>
  <div class="photo strip c" role="img" aria-label="Bright studio living area"></div>
  <div class="abs find-more">FIND OUT MORE</div>
  <span class="abs vsep" style="left:178px"></span>
  <div class="abs contact" style="left:196px">
    <div>
      <svg width="7" height="7" viewBox="0 0 10 10"><path d="M2 0l2 2-1 2c1 1 2 2 3 3l2-1 2 2-2 2C4 10 0 6 0 2z" fill="#fff"/></svg>1300 555 018</div>
    <div><span class="ico-dot"></span>harbourlight_homes</div>
  </div>
  <span class="abs vsep" style="left:336px"></span>
  <div class="abs contact" style="left:346px">
    <div><svg width="8" height="6" viewBox="0 0 10 7"><rect width="10" height="7" fill="#fff"/><path d="M0 0l5 4 5-4" stroke="#2f82b5" fill="none"/></svg>info@harbourlightliving.com.au</div>
    <div><span class="ico-dot"></span>harbourlightliving.com.au</div>
  </div>
</section>

<!-- Emergency contact -->
<section class="page emergency" style="left:627px;top:93px">
  <div class="brand"><span class="brand-dot"></span><span class="brand-name">HARBOURLIGHT LIVING</span></div>
  <div class="abs panel"></div>
  <div class="abs pill">EMERGENCY CONTACT</div>
  <div class="abs col c1">
    <p><b>National Emergency Line:</b> 000</p>
    <p><b>Westgate Police Station:</b><br>(02) 9555 0142 | Open 24 hrs</p>
    <p><b>Elm Grove Medical Centre:</b><br>(02) 9555 0178 | Mon - Fri | 9am - 9pm<br>| Sat - Sun | 9am - 1pm</p>
  </div>
  <span class="abs mid"></span>
  <div class="abs col c2">
    <p><b>Riverside Council:</b> (02) 9555 0100 |<br>Open Mon - Fri | 8.30am - 5pm</p>
    <p><b>St Aldric Hospital :</b> (02) 9555<br>0190 | Open 24 hrs</p>
    <p><b>HomeAccess Line:</b> (1300) 555 044 |<br>Open Mon - Fri | 9am - 5.30pm</p>
  </div>
  <div class="abs site">harbourlightliving.com.au</div>
</section>

<!-- Unit images 01 -->
<section class="page gallery" style="left:75px;top:871px">
  <div class="abs frame"></div>
  <h2 class="abs"><span class="inner">&nbsp;&nbsp;<span class="blue">UNIT</span> IMAGES&nbsp;&nbsp;</span></h2>
  <figure class="tile tone-wall" style="left:34px;top:86px;width:428px;height:183px" role="img" aria-label="Wall-mounted video intercom and air-conditioning controller"><figcaption>INTERCOM, SECURITY &amp; AIR-CONDITIONING</figcaption></figure>
  <figure class="tile tone-bath" style="left:34px;top:294px;width:191px;height:140px" role="img" aria-label="Accessible bathroom with mirror and vanity"><figcaption>ACCESSIBLE BATHROOM</figcaption></figure>
  <figure class="tile tone-green" style="left:269px;top:294px;width:192px;height:140px" role="img" aria-label="Window with vertical screens over garden greenery"><figcaption>WITHOUT BALCONY</figcaption></figure>
  <figure class="tile tone-view" style="left:34px;top:456px;width:191px;height:141px" role="img" aria-label="Level 3 balcony looking over rooftops"><figcaption>BALCONY SPACE LVL 3</figcaption></figure>
  <figure class="tile tone-green" style="left:269px;top:456px;width:192px;height:141px" role="img" aria-label="Juliette balcony with sliding door"><figcaption>JULIETTE BALCONY</figcaption></figure>
  <div class="page-foot">
    <div class="brand"><span class="brand-dot"></span><span class="brand-name">HARBOURLIGHT LIVING</span></div>
    <span class="abs rule"></span>
    <div class="abs tab">harbourlightliving.com.au</div>
    <div class="abs num">01</div>
  </div>
</section>

<!-- Unit images 02 -->
<section class="page gallery" style="left:627px;top:871px">
  <div class="abs frame"></div>
  <h2 class="abs"><span class="inner">&nbsp;&nbsp;<span class="blue">UNIT</span> IMAGES&nbsp;&nbsp;</span></h2>
  <figure class="tile tone-room" style="left:33px;top:82px;width:192px;height:151px" role="img" aria-label="Studio with wall television and glass doors"><figcaption>WITHOUT BALCONY</figcaption></figure>
  <figure class="tile tone-room" style="left:268px;top:82px;width:192px;height:151px" role="img" aria-label="Studio kitchen and dining table"><figcaption>WITHOUT BALCONY</figcaption></figure>
  <figure class="tile tone-room" style="left:33px;top:265px;width:192px;height:149px" role="img" aria-label="Studio bed beside window and wardrobe"><figcaption>WITHOUT BALCONY</figcaption></figure>
  <figure class="tile tone-view" style="left:268px;top:265px;width:192px;height:149px" role="img" aria-label="Large window looking out to sky and brick building"><figcaption>WITHOUT BALCONY</figcaption></figure>
  <figure class="tile tone-bath" style="left:33px;top:450px;width:192px;height:149px" role="img" aria-label="Bathroom toilet with glass screen"><figcaption>WITHOUT BALCONY</figcaption></figure>
  <figure class="tile tone-kitchen" style="left:268px;top:450px;width:192px;height:149px" role="img" aria-label="Standard kitchen with sink and cooktop"><figcaption>STANDARD KITCHEN</figcaption></figure>
  <div class="page-foot">
    <div class="brand"><span class="brand-dot"></span><span class="brand-name">HARBOURLIGHT LIVING</span></div>
    <span class="abs rule"></span>
    <div class="abs tab">harbourlightliving.com.au</div>
    <div class="abs num">02</div>
  </div>
</section>

<!-- Transport -->
<section class="page transport" style="left:353px;top:1635px">
  <div class="abs head"><h2>PUBLIC TRANSPORT, SHOPS &amp; FACILITIE</h2></div>
  <div class="abs acc1"></div>
  <div class="abs acc2"></div>
  <div class="photo map" role="img" aria-label="Street map around the apartments showing the station, bus stops, shops and walking routes"></div>
  <div class="abs lead">LESS THAN 5MIN WALK TO VARIOUS RESTAURANTS, CAFES AND<br><span>OTHER SHOPS IN YOUR LOCAL AREA.</span></div>

  <div class="place l" style="left:43px;top:369px"><span class="name"><i></i>CORNER PHARMACY</span><span class="time">1 Min Walk</span></div>
  <div class="place l" style="left:43px;top:392px"><span class="name"><i></i>FRESHMART GROCER</span><span class="time">2 Min Walk</span></div>
  <div class="place l" style="left:43px;top:416px"><span class="name"><i></i>PULSE FITNESS 24/7<br>PETERSHAM</span><span class="time">2 Min Walk</span></div>
  <div class="place r" style="left:267px;top:370px"><span class="name"><i></i>ELM GROVE<br>MEDICAL CENTRE</span><span class="time">4 Min Walk</span></div>
  <div class="place r" style="left:267px;top:396px"><span class="name"><i></i>BRIGHTSIDE DENTAL<br>PRACTICE</span><span class="time">1 Min Walk</span></div>

  <div class="abs bus-band"></div>
  <div class="abs bus-tab">LOCAL BUS ROUTES</div>
  <div class="bus" style="top:487px"><span class="code">B<sup>1</sup></span><span class="route">428</span><span class="dots" style="flex:0 0 74px"></span><span class="stop">New Canterbury Rd at West St | 5 Min Walk</span><span class="dots"></span><span class="walk">5 Min Walk</span></div>
  <div class="bus" style="top:504px"><span class="code">B<sup>2</sup></span><span class="route">428</span><span class="dots" style="flex:0 0 74px"></span><span class="stop">Audley St opp Fisher St | 1 Min Walk</span><span class="dots"></span><span class="walk">1 Min Walk</span></div>
  <div class="bus" style="top:522px"><span class="code">B<sup>3</sup></span><span class="route">428</span><span class="route">428</span><span class="route">428</span><span class="dots" style="flex:0 0 6px"></span><span class="stop">Petersham Station at Trafalgar St | 3 Min Walk</span><span class="dots"></span><span class="walk">3 Min Walk</span></div>
  <div class="bus" style="top:539px"><span class="code">B<sup>4</sup></span><span class="route">428</span><span class="dots" style="flex:0 0 74px"></span><span class="stop">New Canterbury Rd before Livingstone Rd | 3 Min Walk</span><span class="dots"></span><span class="walk">3 Min Walk</span></div>

  <div class="abs notes">
    <b>Petersham to Southbank Mall</b> (17 mins) = 5 min walk to 6 stops to Enmore Park (7 mins) &gt; 5 min walk Southbank Mall<br>
    <b>Petersham to Central</b> (15 mins) = 4 min walk to Petersham &gt; Platform 1 &gt; 5 stops to Central (11 mins)<br>
    <b>Petersham to Northgate Plaza</b> (14mins) = 1 min walk to &gt; 9 stops to Flood St (12 mins) &gt; 1 min walk Northgate Plaza<br>
    <b>Petersham to Newtown (8 mins)</b> = 4 min walk to Petersham &gt; Platform 1 &gt; 2 stops to Newtown (4 mins)
  </div>
  <div class="page-foot">
    <div class="brand"><span class="brand-dot"></span><span class="brand-name">HARBOURLIGHT LIVING</span></div>
    <span class="abs rule"></span>
    <div class="abs tab">harbourlightliving.com.au</div>
    <div class="abs num">03</div>
  </div>
</section>

</body>
</html>
```